Ridgeline Provisions Co Website Creation

We need a website designed that goes along with our western/cattle brand vibe that our logo has. We are going to need a couple different pages including: About Us, Meat Boxes, Recipes, Contact Us.

We are going to need a shop so that people may visit the website and order meat boxes to be shipped or delivered at their home. Our mission is to provide the highest quality meat that every family can afford.

Would love to see the website design with lots of mountain range backgrounds and create a feel of open range beef that has a tradition of providing great beef. Family owned business that has been raising cattle for over 30 years.

Love the colors of using dark greens, browns, Tans, Blacks

```html
<!DOCTYPE html>
<html lang="en">
<head>
<meta charset="utf-8">
<title>Ridgeline Provisions Co</title>
<link rel="stylesheet" href="https://fonts.googleapis.com/css2?family=Poppins:wght@400;500;600;700&display=swap">
<style>
:root{
  --green:#0c4710;
  --green-dark:#093a0c;
  --brown:#3e1a08;
  --brown-text:#3d1508;
  --cream:#fdf3ee;
  --card:#fdf4ef;
  --white:#ffffff;
  --ink:#222222;
}
*{box-sizing:border-box;margin:0;padding:0}
html,body{width:1200px;height:4827px;overflow:hidden}
body{position:relative;font-family:'Poppins',sans-serif;color:var(--ink);background:var(--white)}
.abs{position:absolute}
.center{left:0;right:0;text-align:center}
.btn{position:absolute;display:flex;align-items:center;justify-content:center;gap:14px;font-weight:600;font-size:19px;text-transform:uppercase}
.btn svg{width:38px;height:12px}

/* header */
.header{top:0;left:0;width:1200px;height:124px;background:var(--white)}
.topbar{top:10px;font-size:14px;color:#333;display:flex;align-items:center;gap:8px}
.nav a{position:absolute;top:72px;font-size:14px;color:#222;text-decoration:none;transform:translateX(-50%);white-space:nowrap}
.nav a.active{color:var(--brown-text);font-weight:600;border-bottom:2px solid var(--brown-text);padding-bottom:4px}
.brand-badge{top:-6px;left:65px;width:256px;height:256px;border-radius:50%;background:var(--white);display:flex;align-items:center;justify-content:center;text-align:center;z-index:3}
.brand-name{font-weight:700;color:var(--green);font-size:27px;line-height:1.1;letter-spacing:1px;text-transform:uppercase}

/* hero */
.hero{top:124px;left:0;width:1200px;height:757px;background:var(--green);overflow:hidden}
.hero-title{top:210px;left:66px;font-size:84px;font-weight:700;color:var(--white);line-height:1}
.hero-sub{top:324px;left:66px;font-size:25px;color:var(--white);line-height:38px}
.btn-light{background:var(--white);color:var(--ink)}
.btn-outline{border:3px solid var(--white);color:var(--white)}
.dots{top:670px;left:572px;display:flex;gap:4px}
.dots span{width:12px;height:12px;border-radius:50%;background:#c9c9c9}
.dots span:first-child{background:var(--white)}

/* section titles */
.sec-title{font-size:62px;font-weight:700;text-transform:uppercase;line-height:1}
.sec-sub{display:flex;align-items:center;justify-content:center;gap:16px;font-size:26px}
.sec-sub i{display:block;width:88px;height:4px}

/* why */
.why{top:881px;left:0;width:1200px;height:578px;background:var(--white)}
.card{position:absolute;top:325px;width:264px;height:146px;border:1px solid #b9a49a;border-radius:14px;background:var(--card);text-align:center}
.card p{position:absolute;left:0;right:0;top:80px;font-size:20px;font-weight:600;color:#222}
.card-icon{position:absolute;left:50%;top:-55px;margin-left:-55px;width:110px;height:110px;border-radius:50%;background:var(--brown);border:4px solid var(--white);box-shadow:0 0 0 2px #b9a49a;display:flex;align-items:center;justify-content:center}

/* services */
.services{top:1459px;left:0;width:1200px;height:926px;background:var(--brown)}
.photo-card{position:absolute;top:281px;width:344px;height:399px;border-radius:36px;border:3px solid var(--white)}
.photo-label{position:absolute;top:709px;width:344px;text-align:center;color:var(--white);font-size:20px}
.round-btn{position:absolute;top:810px;width:44px;height:44px;border-radius:50%;display:flex;align-items:center;justify-content:center}

/* how */
.how{top:2385px;left:0;width:1200px;height:649px;background:var(--cream)}
.step{position:absolute;top:274px;width:112px;height:112px;border-radius:50%;background:var(--green);border:4px solid var(--white);box-shadow:0 0 0 2px var(--green);color:var(--white);font-size:52px;font-weight:600;display:flex;align-items:center;justify-content:center}
.step-label{position:absolute;top:404px;width:300px;text-align:center;font-size:20px;font-weight:600;color:#222}

/* online */
.online{top:3034px;left:0;width:1200px;height:626px;background:radial-gradient(ellipse at 55% 50%,#6b2a22 0%,#4a1d17 45%,#24100c 100%)}
.online-title{top:178px;font-size:56px;font-weight:600;color:var(--white);line-height:68px;text-transform:uppercase}

/* about */
.about{top:3660px;left:0;width:1200px;height:671px;background:var(--white)}
.about-photo{position:absolute;right:0;top:0;width:560px;height:671px;background:linear-gradient(180deg,#cfdbe6 0%,#b6c3cc 40%,#8ea05a 72%,#6b8a3a 100%)}
.about-fade{position:absolute;left:640px;top:0;width:160px;height:671px;background:linear-gradient(90deg,#ffffff 0%,rgba(255,255,255,0) 100%)}
.about-text{top:290px;left:68px;width:586px;font-size:14px;line-height:29px;color:#333;text-align:justify}

/* newsletter + footer */
.footer{top:4331px;left:0;width:1200px;height:496px;background:var(--green)}
.field{position:absolute;top:133px;height:42px;background:var(--white);font-size:11px;color:#777;padding:14px 36px}
.foot-item{position:absolute;top:262px;display:flex;align-items:flex-start;gap:14px;color:var(--white);font-size:13px;line-height:17px}
.foot-icon{width:22px;height:22px;background:var(--white);border-radius:3px;display:flex;align-items:center;justify-content:center;margin-top:6px}
.foot-nav a{position:absolute;top:350px;color:var(--white);font-size:14px;text-decoration:none;transform:translateX(-50%);white-space:nowrap}
.social{position:absolute;top:460px;width:24px;height:24px;border-radius:50%;border:1.5px solid var(--white)}
</style>
</head>
<body>

<header class="abs header">
  <div class="abs topbar" style="left:772px">
    <svg width="16" height="16" viewBox="0 0 24 24" fill="#333"><path d="M6.6 10.8a15 15 0 0 0 6.6 6.6l2.2-2.2c.3-.3.7-.4 1-.2 1.1.4 2.3.6 3.6.6.6 0 1 .4 1 1V20c0 .6-.4 1-1 1A17 17 0 0 1 3 4c0-.6.4-1 1-1h3.5c.6 0 1 .4 1 1 0 1.3.2 2.5.6 3.6.1.3 0 .7-.2 1z"/></svg>
    <span>555 014 2290</span>
  </div>
  <div class="abs topbar" style="left:938px">
    <svg width="18" height="14" viewBox="0 0 24 18" fill="#333"><path d="M0 0h24v18H0z"/><path d="M1 1l11 9 11-9" stroke="#fff" stroke-width="2" fill="none"/></svg>
    <span>hello@ridgelineprov.com</span>
  </div>
  <nav class="nav">
    <a class="active" style="left:414px">HOME</a>
    <a style="left:542px">ABOUT US</a>
    <a style="left:692px">MEAT BOXES</a>
    <a style="left:825px">SHOP</a>
    <a style="left:943px">RECIPES</a>
    <a style="left:1088px">CONTACT US</a>
  </nav>
</header>

<div class="abs brand-badge"><div class="brand-name">Ridgeline<br>Provisions<br>Co</div></div>

<section class="abs hero">
  <svg class="abs" style="left:540px;top:0" width="660" height="757" viewBox="0 0 660 757" role="img" aria-label="Raw cuts of beef on a wooden board">
    <defs>
      <radialGradient id="meatGrad" cx="55%" cy="45%" r="70%">
        <stop offset="0" stop-color="#c9575a"/>
        <stop offset="0.5" stop-color="#b54a44"/>
        <stop offset="1" stop-color="#8a4a2c"/>
      </radialGradient>
    </defs>
    <path d="M230 0 H660 V757 H130 C40 640 0 480 10 360 C25 200 110 70 230 0 Z" fill="url(#meatGrad)"/>
  </svg>
  <h1 class="abs hero-title">RIDGELINE</h1>
  <p class="abs hero-sub">Family owned business that has been<br>raising cattle for over 30 years.</p>
  <a class="btn btn-light" style="top:444px;left:69px;width:210px;height:70px">Shop Meat <svg viewBox="0 0 38 12"><path d="M0 6h35M30 1l6 5-6 5" stroke="#222" stroke-width="2" fill="none"/></svg></a>
  <a class="btn btn-outline" style="top:444px;left:292px;width:210px;height:70px">About Us <svg viewBox="0 0 38 12"><path d="M0 6h35M30 1l6 5-6 5" stroke="#fff" stroke-width="2" fill="none"/></svg></a>
  <div class="abs dots"><span></span><span></span><span></span><span></span></div>
</section>

<section class="abs why">
  <h2 class="abs center sec-title" style="top:124px;color:var(--brown-text)">Why Choose Us?</h2>
  <div class="abs center sec-sub" style="top:190px;color:var(--brown-text)"><i style="background:var(--green)"></i>Ridgeline Provisions<i style="background:var(--green)"></i></div>
  <div class="card" style="left:66px">
    <div class="card-icon"><svg width="52" height="34" viewBox="0 0 52 34"><rect x="2" y="4" width="30" height="20" rx="2" fill="#fff"/><path d="M32 10h10l8 8v6H32z" fill="#fff"/><circle cx="12" cy="27" r="5" fill="#fff" stroke="#3e1a08" stroke-width="2"/><circle cx="40" cy="27" r="5" fill="#fff" stroke="#3e1a08" stroke-width="2"/></svg></div>
    <p>Free Delivery</p>
  </div>
  <div class="card" style="left:336px">
    <div class="card-icon"><svg width="44" height="44" viewBox="0 0 44 44" fill="none" stroke="#fff" stroke-width="4"><path d="M34 24v14H6V10h18"/><path d="M14 22l8 8 18-20"/></svg></div>
    <p>Best Quality</p>
  </div>
  <div class="card" style="left:604px">
    <div class="card-icon"><span style="color:#fff;font-size:56px;font-weight:700;line-height:1">$</span></div>
    <p>Affordable Price</p>
  </div>
  <div class="card" style="left:872px">
    <div class="card-icon"><svg width="48" height="40" viewBox="0 0 48 40" fill="none" stroke="#fff" stroke-width="3"><rect x="2" y="2" width="40" height="30"/><path d="M9 11h26M9 18h18M9 25h12"/><circle cx="36" cy="28" r="6" fill="#3e1a08"/></svg></div>
    <p>5 Years of Experience</p>
  </div>
</section>

<section class="abs services">
  <h2 class="abs center sec-title" style="top:125px;color:var(--white)">Our Services</h2>
  <div class="abs center sec-sub" style="top:191px;color:var(--white)"><i style="background:var(--white)"></i>What We Do<i style="background:var(--white)"></i></div>
  <div class="photo-card" style="left:68px;background:radial-gradient(ellipse at 50% 45%,#b42a36 0%,#7a1e26 35%,#2a2a2c 70%)" role="img" aria-label="Diced beef cubes on a dark slate"></div>
  <div class="photo-card" style="left:429px;background:radial-gradient(ellipse at 50% 60%,#9e1c26 0%,#5c1418 35%,#1a1a1a 70%)" role="img" aria-label="Beef fillet steaks with rosemary on a dark background"></div>
  <div class="photo-card" style="left:789px;background:radial-gradient(ellipse at 50% 50%,#d2646a 0%,#b74c4e 40%,#8a5634 80%)" role="img" aria-label="Raw beef roast with dill on a wooden board"></div>
  <div class="photo-label" style="left:68px">MEAT 1</div>
  <div class="photo-label" style="left:429px">MEAT 2</div>
  <div class="photo-label" style="left:789px">MEAT 3</div>
  <div class="round-btn" style="left:552px;border:2px solid var(--white)"><svg width="18" height="12" viewBox="0 0 18 12"><path d="M17 6H2M6 1L1 6l5 5" stroke="#fff" stroke-width="2" fill="none"/></svg></div>
  <div class="round-btn" style="left:602px;background:var(--white)"><svg width="18" height="12" viewBox="0 0 18 12"><path d="M1 6h15M12 1l5 5-5 5" stroke="#3e1a08" stroke-width="2" fill="none"/></svg></div>
</section>

<section class="abs how">
  <h2 class="abs center sec-title" style="top:126px;color:var(--brown-text)">How It Works</h2>
  <div class="abs center sec-sub" style="top:192px;color:var(--brown-text)"><i style="background:var(--green)"></i>Ridgeline Provisions<i style="background:var(--green)"></i></div>
  <div class="step" style="left:86px">1</div>
  <div class="step" style="left:390px">2</div>
  <div class="step" style="left:696px">3</div>
  <div class="step" style="left:996px">4</div>
  <svg class="abs" style="left:0;top:280px" width="1200" height="60" viewBox="0 0 1200 60" fill="none" stroke="#222" stroke-width="2" stroke-dasharray="6 5">
    <path d="M226 30 C270 0 330 0 364 28"/><path d="M530 30 C574 0 634 0 668 28"/><path d="M836 30 C880 0 940 0 972 28"/>
    <g stroke-dasharray="none"><path d="M356 22l9 7-11 2"/><path d="M660 22l9 7-11 2"/><path d="M964 22l9 7-11 2"/></g>
  </svg>
  <div class="step-label" style="left:-8px">Find a Meat Shop</div>
  <div class="step-label" style="left:296px">Select Your Beef</div>
  <div class="step-label" style="left:602px">Place Your Order</div>
  <div class="step-label" style="left:902px">Receive Your Beef</div>
  <a class="btn" style="top:487px;left:488px;width:224px;height:70px;background:var(--brown);color:var(--white)">Book Now <svg viewBox="0 0 38 12"><path d="M0 6h35M30 1l6 5-6 5" stroke="#fff" stroke-width="2" fill="none"/></svg></a>
</section>

<section class="abs online" role="img" aria-label="Dimly lit raw beef with tomatoes, lemon and peppercorns">
  <h2 class="abs center online-title">Online Food Delivery Anytime<br>In Your House</h2>
  <div class="abs center sec-sub" style="top:336px;color:var(--white)"><i style="background:var(--white);width:88px;height:3px"></i>We are believe in your time value<i style="background:var(--white);width:88px;height:3px"></i></div>
  <a class="btn btn-light" style="top:433px;left:461px;width:278px;height:77px">Order Online <svg viewBox="0 0 38 12"><path d="M0 6h35M30 1l6 5-6 5" stroke="#222" stroke-width="2" fill="none"/></svg></a>
</section>

<section class="abs about">
  <div class="about-photo" role="img" aria-label="Brown and white cow grazing in a mountain meadow under a cloudy sky"></div>
  <div class="about-fade"></div>
  <h2 class="abs sec-title" style="top:140px;left:66px;color:var(--brown-text)">About Ridgeline</h2>
  <div class="abs" style="top:204px;left:68px;display:flex;align-items:center;gap:14px;font-size:25px;color:var(--brown-text)">Who We Are<i style="display:block;width:88px;height:4px;background:var(--green)"></i></div>
  <p class="abs about-text">Lorem ipsum dolor sit amet, consectetur adipiscing elit, sed do eiusmod tempor incididunt ut labore et dolore magna aliqua. Quis ipsum suspendisse ultrices gravida. Risus commodo viverra maecenas accumsan lacus vel facilisis. Lorem ipsum dolor sit amet, consectetur adipiscing elit, sed do eiusmod tempor incididunt ut labore et dolore magna aliqua. Quis ipsum suspendisse ultrices gravida. Risus commodo viverra maecenas accumsan lacus vel facilisis.</p>
  <a class="btn" style="top:488px;left:69px;width:210px;height:69px;background:var(--green);color:var(--white)">Read More <svg viewBox="0 0 38 12"><path d="M0 6h35M30 1l6 5-6 5" stroke="#fff" stroke-width="2" fill="none"/></svg></a>
</section>

<footer class="abs footer">
  <h3 class="abs center" style="top:74px;color:var(--white);font-size:30px;font-weight:600">Subscribe to Our Newsletter</h3>
  <div class="field" style="left:244px;width:270px">Enter Name</div>
  <div class="field" style="left:523px;width:272px">Email Address</div>
  <div class="abs" style="top:133px;left:806px;width:150px;height:42px;background:var(--brown);color:var(--white);font-size:14px;font-weight:600;display:flex;align-items:center;justify-content:center">SUBSCRIBE</div>

  <div class="abs" style="top:238px;left:40px;width:220px;text-align:center"><div class="brand-name" style="color:var(--white);font-size:24px">Ridgeline<br>Provisions<br>Co</div></div>

  <div class="foot-item" style="left:459px"><div class="foot-icon"><svg width="12" height="12" viewBox="0 0 24 24" fill="#0c4710"><path d="M6.6 10.8a15 15 0 0 0 6.6 6.6l2.2-2.2c.3-.3.7-.4 1-.2 1.1.4 2.3.6 3.6.6.6 0 1 .4 1 1V20c0 .6-.4 1-1 1A17 17 0 0 1 3 4c0-.6.4-1 1-1h3.5c.6 0 1 .4 1 1 0 1.3.2 2.5.6 3.6.1.3 0 .7-.2 1z"/></svg></div><div>CALL US<br>555 014 2290</div></div>
  <div class="foot-item" style="left:654px"><div class="foot-icon"><svg width="12" height="10" viewBox="0 0 24 18"><path d="M0 0h24v18H0z" fill="#0c4710"/><path d="M1 1l11 9 11-9" stroke="#fff" stroke-width="2" fill="none"/></svg></div><div>EMAIL US<br>hello@ridgelineprov.com</div></div>
  <div class="foot-item" style="left:911px"><div class="foot-icon"><svg width="10" height="14" viewBox="0 0 20 28" fill="#0c4710"><path d="M10 0a10 10 0 0 0-10 10c0 8 10 18 10 18s10-10 10-18A10 10 0 0 0 10 0zm0 14a4 4 0 1 1 0-8 4 4 0 0 1 0 8z"/></svg></div><div>Address line Dummy Here<br>Address line Here</div></div>
  <div class="abs" style="top:319px;left:398px;width:738px;height:1px;background:rgba(255,255,255,.45)"></div>
  <nav class="foot-nav">
    <a style="left:673px">HOME</a><a style="left:759px">ABOUT US</a><a style="left:869px">MEAT BOXES</a><a style="left:979px">RECIPES</a><a style="left:1087px">CONTACT US</a>
  </nav>
  <div class="abs" style="top:424px;left:0;width:1200px;height:1px;background:rgba(255,255,255,.35)"></div>
  <p class="abs" style="top:463px;left:66px;color:var(--white);font-size:11px">Copyright ©2024- All Rights Reserved by Company name</p>
  <span class="social" style="left:1024px"></span><span class="social" style="left:1053px"></span><span class="social" style="left:1082px"></span><span class="social" style="left:1111px"></span>
</footer>

</body>
</html>
```